Professional Modern Website Design

We are a premium IT services provider to the financial industry based in London. Our company is called Velmar our current holding page is www.velmar.co.uk. We require a new website to match our new corporate identity. This project is for the design phase only. Development will be handled in-house. I have attached examples of wire frames we have developed (although open to suggestions for improvement) Our brand document that should demonstrate current brand, inc how we communicate to potential clients and finally mostly completed web-content.
We are looking for designers that can create something that sets us apart from our competitors.
Target Market(s)
IT Decision makers in Finance companies such as; hedge funds, private investment banks etc
Industry/Entity Type
Financial
Number of Pages Required
5+ page
Requirements
Must have
- hexagon elements in the design, unique design.
Nice to have
- Blog and social media feeds
Should not have
- Should not resemble a downloaded template

```html
<!DOCTYPE html>
<html lang="en">
<head>
<meta charset="utf-8">
<title>Velmar – Systems Integration for Finance</title>
<link rel="stylesheet" href="https://fonts.googleapis.com/css2?family=Roboto+Condensed:wght@400;700&family=Open+Sans:wght@400;600&display=swap">
<style>
:root{
  --orange:#f47b20;
  --dark:#1f1f1f;
  --darker:#161616;
  --header:#2a2a2a;
  --light:#efefef;
  --white:#ffffff;
  --bar:#5a5a5a;
  --text:#5c5c5c;
  --muted:#8a8a8a;
  --footer-text:#c9c9c9;
  --field:#e9e9e9;
}
*{box-sizing:border-box;margin:0;padding:0}
html,body{width:1200px;height:2188px;overflow:hidden}
body{position:relative;background:var(--light);font-family:"Open Sans",Arial,sans-serif;color:var(--text)}
.head-font{font-family:"Roboto Condensed","Arial Narrow",sans-serif}

/* header */
.site-header{position:absolute;left:0;top:0;width:1200px;height:200px;background:linear-gradient(180deg,#3a3a3a 0%,#262626 100%)}
.brand{position:absolute;left:73px;top:34px;display:flex;align-items:center;gap:12px}
.brand-mark{width:34px;height:34px;background:var(--orange)}
.brand-name{font-family:"Roboto Condensed","Arial Narrow",sans-serif;font-weight:700;font-size:34px;letter-spacing:4px;color:var(--white)}
.office-phone{position:absolute;top:56px;display:flex;align-items:center;gap:12px}
.office-phone.london{left:672px}
.office-phone.essex{left:924px}
.office-phone .label{font-family:"Roboto Condensed","Arial Narrow",sans-serif;font-size:14px;color:var(--orange);line-height:16px}
.office-phone .number{font-family:"Roboto Condensed","Arial Narrow",sans-serif;font-size:21px;color:var(--white);line-height:24px}
.main-nav{position:absolute;left:0;top:164px;width:1200px;height:36px;background:var(--orange)}
.main-nav a{position:absolute;top:0;line-height:36px;font-family:"Roboto Condensed","Arial Narrow",sans-serif;font-weight:700;font-size:16px;color:var(--white);text-decoration:none}
.social{position:absolute;right:76px;top:11px;display:flex;gap:12px}
.social span{width:14px;height:14px;background:var(--white)}

/* hero */
.hero{position:absolute;left:0;top:200px;width:1200px;height:524px;background:linear-gradient(180deg,#2b2b2b,#1c1c1c)}
.hero-panel{position:absolute;left:73px;top:19px;width:1052px;height:481px;border:7px solid var(--white);background:linear-gradient(90deg,#f4f4f4 0%,#e4e4e4 40%,#cfcfcf 70%,#9d9d9d 100%);overflow:hidden}
.hero-photo{position:absolute;right:0;top:0;width:470px;height:467px;background:radial-gradient(ellipse at 55% 40%,#d9d9d9 0%,#a8a8a8 55%,#6e6e6e 100%)}
.hero-copy{position:absolute;left:59px;top:84px;width:360px}
.hero-copy h1{font-family:"Roboto Condensed","Arial Narrow",sans-serif;font-weight:700;font-size:25px;line-height:28px;color:var(--darker)}
.hero-copy p{margin-top:42px;font-size:14.5px;line-height:27px;color:#333}
.btn{display:inline-block;background:var(--orange);color:var(--white);font-family:"Roboto Condensed","Arial Narrow",sans-serif;font-size:15px;text-decoration:none;text-align:center}
.hero-copy .btn{margin-top:28px;width:104px;height:36px;line-height:36px}

/* audience */
.audience{position:absolute;left:0;top:724px;width:1200px;height:892px;background:var(--light)}
.audience h2{position:absolute;top:40px;width:100%;text-align:center;font-family:"Roboto Condensed","Arial Narrow",sans-serif;font-weight:700;font-size:26px;color:var(--darker)}
.audience .intro{position:absolute;top:82px;left:300px;width:600px;text-align:center;font-size:15px;line-height:26px;color:var(--muted)}
.role-card{position:absolute;top:197px;width:268px;height:330px}
.role-card::before{content:"";position:absolute;left:0;top:151px;width:268px;height:452px;background:var(--white);box-shadow:0 12px 14px -8px rgba(0,0,0,.25)}
.role-card svg{position:absolute;left:24px;top:0;width:220px;height:244px}
.role-title{position:absolute;left:0;top:255px;width:268px;height:59px;background:var(--bar);color:var(--white);font-family:"Roboto Condensed","Arial Narrow",sans-serif;font-weight:700;font-size:17px;line-height:19px;display:flex;align-items:center;justify-content:center;text-align:center;padding:0 30px}
.role-text{position:absolute;left:18px;top:327px;width:232px;font-size:13px;line-height:22px;text-align:center;color:var(--text)}

/* footer */
.site-footer{position:absolute;left:0;top:1616px;width:1200px;height:572px;background:var(--dark);border-top:4px solid var(--orange);color:var(--footer-text)}
.footer-mark{position:absolute;left:586px;top:-28px;width:28px;height:28px;border-radius:50%;background:var(--orange);top:-24px}
.footer-title{position:absolute;top:60px;width:100%;text-align:center;font-family:"Roboto Condensed","Arial Narrow",sans-serif;font-weight:700;font-size:25px;color:var(--white)}
.footer-title::after{content:"";display:block;width:40px;height:3px;background:var(--orange);margin:8px auto 0}
.office{position:absolute;top:126px}
.office h3,.footer-col h3{font-family:"Roboto Condensed","Arial Narrow",sans-serif;font-weight:700;font-size:15px;color:var(--white)}
.office .line{position:absolute;top:36px;display:flex;gap:10px;font-family:"Roboto Condensed","Arial Narrow",sans-serif;font-size:13.5px;line-height:19px;white-space:nowrap}
.office .line svg{flex:none;margin-top:2px}
.office .k{color:var(--orange)}
.divider{position:absolute;left:602px;top:120px;width:1px;height:90px;background:#3a3a3a}
.footer-col{position:absolute;top:244px;width:250px}
.post{margin-top:24px;padding-bottom:20px;border-bottom:1px solid #333}
.post .date{font-family:"Roboto Condensed","Arial Narrow",sans-serif;font-size:12px;color:#777}
.post .headline{margin-top:6px;font-family:"Roboto Condensed","Arial Narrow",sans-serif;font-size:13.5px;line-height:19px;color:var(--footer-text)}
.post + .post{margin-top:30px;border-bottom:none}
.contact-form{position:absolute;left:613px;top:244px;width:513px}
.contact-form .row{display:flex;gap:8px;margin-top:18px}
.field{background:var(--field);height:31px;flex:1;padding:8px 10px;font-family:"Roboto Condensed","Arial Narrow",sans-serif;font-size:12.5px;color:#666}
.field.message{display:block;height:176px;margin-top:9px}
.contact-form .btn{margin-top:11px;width:106px;height:33px;line-height:33px}
.copyright{position:absolute;left:73px;top:520px;font-family:"Roboto Condensed","Arial Narrow",sans-serif;font-size:12.5px;color:var(--footer-text)}
</style>
</head>
<body>

<header class="site-header">
  <div class="brand"><span class="brand-mark"></span><span class="brand-name">VELMAR</span></div>

  <div class="office-phone london">
    <svg width="40" height="44" viewBox="0 0 40 44"><polygon points="20,2 38,12 38,32 20,42 2,32 2,12" fill="none" stroke="#fff" stroke-width="1.5"/><path d="M14 15c1-1 2-1 3 0l2 3-2 2c1 2 3 4 5 5l2-2 3 2c1 1 1 2 0 3-3 3-8 0-11-4s-5-7-2-9z" fill="#fff"/></svg>
    <div><div class="label">LONDON</div><div class="number">+44 20 7946 0182</div></div>
  </div>
  <div class="office-phone essex">
    <svg width="40" height="44" viewBox="0 0 40 44"><polygon points="20,2 38,12 38,32 20,42 2,32 2,12" fill="none" stroke="#fff" stroke-width="1.5"/><path d="M14 15c1-1 2-1 3 0l2 3-2 2c1 2 3 4 5 5l2-2 3 2c1 1 1 2 0 3-3 3-8 0-11-4s-5-7-2-9z" fill="#fff"/></svg>
    <div><div class="label">ESSEX</div><div class="number">+44 20 7946 0185</div></div>
  </div>

  <nav class="main-nav">
    <a href="#" style="left:108px">ABOUT</a>
    <a href="#" style="left:217px">SERVICES</a>
    <a href="#" style="left:348px">PARTNERS</a>
    <a href="#" style="left:482px">CLIENTS</a>
    <a href="#" style="left:598px">CONTACT</a>
    <div class="social"><span></span><span></span><span></span><span></span></div>
  </nav>
</header>

<section class="hero">
  <div class="hero-panel">
    <div class="hero-photo" role="img" aria-label="Smiling businesswoman holding a tablet in a bright office"></div>
    <div class="hero-copy">
      <h1>YOU NEED INTEGRATION.<br>WE’RE ALWAYS THERE WITH YOU.</h1>
      <p>Velmar is one of the leading systems integrators to the world’s finance sector. We are an extension of your business and our services portfolio has been built so you always have access to a complete partner.</p>
      <a class="btn" href="#">ABOUT US</a>
    </div>
  </div>
</section>

<section class="audience">
  <h2>WHO ARE YOU?</h2>
  <p class="intro">If you’re part of a financial organisation, we have the power to help everyone work more efficiently, productively and profitably.</p>

  <article class="role-card" style="left:60px">
    <svg viewBox="0 0 220 244" role="img" aria-label="Portrait of a senior fund manager in a suit">
      <defs><linearGradient id="g1" x1="0" y1="0" x2="0" y2="1"><stop offset="0" stop-color="#c9cdd3"/><stop offset="1" stop-color="#4a5260"/></linearGradient></defs>
      <polygon points="110,4 214,64 214,180 110,240 6,180 6,64" fill="#fff" stroke="#f47b20" stroke-width="8"/>
      <polygon points="110,18 202,71 202,173 110,226 18,173 18,71" fill="url(#g1)"/>
    </svg>
    <div class="role-title">SENIOR HEDGE FUND MANAGER/CEO</div>
    <p class="role-text">You need to develop and implement strategies for business growth, while ensuring profitability. You’re aware your biggest asset is your staff and a happy workforce is a productive one. Security is a key concern in a changing always-on world and you need to be compliant, but you don’t want to over-spend. Velmar can help you find the best solutions to help your business grow at the speed you want it to.</p>
  </article>

  <article class="role-card" style="left:332px">
    <svg viewBox="0 0 220 244" role="img" aria-label="Portrait of a finance director">
      <defs><linearGradient id="g2" x1="0" y1="0" x2="0" y2="1"><stop offset="0" stop-color="#e2e2e2"/><stop offset="1" stop-color="#6d6258"/></linearGradient></defs>
      <polygon points="110,4 214,64 214,180 110,240 6,180 6,64" fill="#fff" stroke="#f47b20" stroke-width="8"/>
      <polygon points="110,18 202,71 202,173 110,226 18,173 18,71" fill="url(#g2)"/>
    </svg>
    <div class="role-title">CFO</div>
    <p class="role-text">Your key responsibility is to obtain the maximum ROI from products and services. You understand investment opportunities, providing they return higher efficiencies and revenues. You are concerned more with long-term spending versus short-term and how you can get the most value out of a proposition. Velmar can advise how to boost ROI by streamlining your business to maximise return.</p>
  </article>

  <article class="role-card" style="left:604px">
    <svg viewBox="0 0 220 244" role="img" aria-label="Portrait of an IT manager in an office">
      <defs><linearGradient id="g3" x1="0" y1="0" x2="0" y2="1"><stop offset="0" stop-color="#eceef0"/><stop offset="1" stop-color="#7f8793"/></linearGradient></defs>
      <polygon points="110,4 214,64 214,180 110,240 6,180 6,64" fill="#fff" stroke="#f47b20" stroke-width="8"/>
      <polygon points="110,18 202,71 202,173 110,226 18,173 18,71" fill="url(#g3)"/>
    </svg>
    <div class="role-title">IT MANAGER/CTO</div>
    <p class="role-text">Integration with partners and services is your key concern. You want to make sure any IT system you implement will work with the whole infrastructure of your company. You don’t want your team to waste valuable time dealing with things that don’t matter. Velmar provides the whole picture to ensure your company is ready for the next generation of IT.</p>
  </article>

  <article class="role-card" style="left:874px">
    <svg viewBox="0 0 220 244" role="img" aria-label="Group of smiling office employees">
      <defs><linearGradient id="g4" x1="0" y1="0" x2="0" y2="1"><stop offset="0" stop-color="#e6e6e6"/><stop offset="1" stop-color="#6a7078"/></linearGradient></defs>
      <polygon points="110,4 214,64 214,180 110,240 6,180 6,64" fill="#fff" stroke="#f47b20" stroke-width="8"/>
      <polygon points="110,18 202,71 202,173 110,226 18,173 18,71" fill="url(#g4)"/>
    </svg>
    <div class="role-title">EMPLOYEES</div>
    <p class="role-text">You’re working hard, but not getting anywhere fast. You want the tools to make your job easier so you can spend more time thinking about what you’re doing rather than how you’re doing it. You shouldn’t have to think about the technology you’re using, because it should just work. Velmar can help you get back on track everyday.</p>
  </article>
</section>

<footer class="site-footer">
  <span class="footer-mark"></span>
  <h2 class="footer-title">GET IN TOUCH</h2>

  <div class="office" style="left:73px">
    <h3>LONDON OFFICE</h3>
    <div class="line" style="left:0">
      <svg width="12" height="16" viewBox="0 0 12 16"><path d="M6 0a6 6 0 0 0-6 6c0 4 6 10 6 10s6-6 6-10a6 6 0 0 0-6-6zm0 8.5a2.5 2.5 0 1 1 0-5 2.5 2.5 0 0 1 0 5z" fill="#777"/></svg>
      <div>18 HARLOW STREET,<br>MAYFAIR, LONDON W1K 2AB</div>
    </div>
    <div class="line" style="left:270px">
      <svg width="13" height="14" viewBox="0 0 13 14"><path d="M2 1c1-1 2-1 3 0l2 3-2 2c1 2 2 3 4 4l2-2 2 2c1 1 1 2 0 3-3 2-8-1-10-4S-1 3 2 1z" fill="#777"/></svg>
      <div><span class="k">T:</span> +44 20 7946 0182<br><span class="k">E:</span> INFO@VELMAR.CO.UK</div>
    </div>
  </div>
  <div class="divider"></div>
  <div class="office" style="left:640px">
    <h3>ESSEX OFFICE</h3>
    <div class="line" style="left:0">
      <svg width="12" height="16" viewBox="0 0 12 16"><path d="M6 0a6 6 0 0 0-6 6c0 4 6 10 6 10s6-6 6-10a6 6 0 0 0-6-6zm0 8.5a2.5 2.5 0 1 1 0-5 2.5 2.5 0 0 1 0 5z" fill="#777"/></svg>
      <div>7 MILL WORKS, MILL AVENUE<br>SOUTHEND, ESSEX SS1 4QT</div>
    </div>
    <div class="line" style="left:296px">
      <svg width="13" height="14" viewBox="0 0 13 14"><path d="M2 1c1-1 2-1 3 0l2 3-2 2c1 2 2 3 4 4l2-2 2 2c1 1 1 2 0 3-3 2-8-1-10-4S-1 3 2 1z" fill="#777"/></svg>
      <div><span class="k">T:</span> +44 20 7946 0185<br><span class="k">E:</span> INFO@VELMAR.CO.UK</div>
    </div>
  </div>

  <div class="footer-col" style="left:73px">
    <h3>RECENT NEWS</h3>
    <div class="post"><div class="date">10 MAR 2015</div><div class="headline">MIRUM EST NOTARE QUAM LITTERA<br>GOTHI CA, QUAM NUNC</div></div>
    <div class="post"><div class="date">10 MAR 2015</div><div class="headline">MIRUM EST NOTARE QUAM LITTERA<br>GOTHI CA, QUAM NUNC</div></div>
  </div>
  <div class="footer-col" style="left:343px">
    <h3>RECENT BLOG</h3>
    <div class="post"><div class="date">10 MAR 2015 | 10 COMMENTS</div><div class="headline">MIRUM EST NOTARE QUAM LITTERA<br>GOTHI CA, QUAM NUNC</div></div>
    <div class="post"><div class="date">10 MAR 2015 | 10 COMMENTS</div><div class="headline">MIRUM EST NOTARE QUAM LITTERA<br>GOTHI CA, QUAM NUNC</div></div>
  </div>

  <form class="contact-form">
    <h3 class="head-font" style="font-weight:700;font-size:15px;color:#fff">CONTACT VELMAR</h3>
    <div class="row"><div class="field">NAME</div><div class="field">EMAIL</div></div>
    <div class="field message">MESSAGE</div>
    <span class="btn">SUBMIT</span>
  </form>

  <p class="copyright">© 2015 VELMAR LIMITED. ALL RIGHTS RESERVED.</p>
</footer>

</body>
</html>
```